Memorial Ledger Suite (Web Design)

Design with your logo. Background in black or dark. Elegant style, it's a website for professional people only. Our company provides a cloud software manager for Funeral Services Companies.

Target Market(s)

Professional of Funeral Services.

Coding

Coded - Design and coding required

Number of Pages Required

3 page

Font styles to use
Sans Serif

Colors
fbee3d
000000
5c5c5c

Requirements
Must have
• Design of the website should be similar to our logo colors.

```html
<!DOCTYPE html>
<html lang="en">
<head>
<meta charset="utf-8">
<title>Memorial Ledger Suite</title>
<link href="https://fonts.googleapis.com/css2?family=Lato:wght@400;700;900&display=swap" rel="stylesheet">
<style>
:root{
  --yellow:#fbee3d;
  --black:#000000;
  --grey:#5c5c5c;
  --dark:#1c1c1c;
  --ink:#222222;
  --light:#ededed;
  --white:#ffffff;
}
*{box-sizing:border-box;margin:0;padding:0}
html,body{width:1200px;height:3732px;overflow:hidden}
body{font-family:'Lato',Arial,sans-serif;color:var(--ink);background:var(--white);position:relative}
.abs{position:absolute}
p{font-size:14px;line-height:1.6}
.btn{display:inline-block;font-size:12px;font-weight:700;letter-spacing:.5px;padding:10px 20px;text-transform:uppercase}
.btn-yellow{background:var(--yellow);color:var(--black)}
.btn-outline{border:2px solid var(--ink);color:var(--ink)}
.section-title{font-size:30px;font-weight:900;text-transform:uppercase;letter-spacing:.5px}

/* header */
.topbar{top:0;left:0;width:1200px;height:44px;display:flex;justify-content:flex-end;align-items:center;gap:28px;padding-right:60px;font-size:13px;color:var(--grey)}
.topbar span{display:flex;align-items:center;gap:8px}
.header{top:44px;left:0;width:1200px;height:96px;border-bottom:1px solid #e5e5e5}
.brand{display:flex;align-items:center;gap:10px;font-weight:900;font-size:22px;color:var(--ink)}
.brand .mark{width:18px;height:18px;background:var(--yellow)}
.header .brand{position:absolute;left:60px;top:22px}
.nav{position:absolute;right:60px;top:26px;display:flex;align-items:center;gap:6px}
.nav a{font-size:12px;font-weight:700;color:var(--ink);padding:14px 16px;text-decoration:none;text-transform:uppercase}
.nav a.active{background:var(--yellow)}
.nav a.login{background:var(--black);color:var(--white);border-radius:4px;padding:10px 18px;margin-left:14px}

/* hero */
.hero{top:140px;left:0;width:1200px;height:590px;background:linear-gradient(100deg,#2b2b2b 0%,#7a7a78 45%,#b9b8b3 70%,#3a3a3a 100%)}
.hero-caption{position:absolute;left:0;width:1200px;top:250px;text-align:center;color:var(--white)}
.hero-caption h1{font-size:50px;font-weight:900;letter-spacing:1px}
.hero-caption p{font-size:17px;margin-top:6px}
.hero-caption .btn{margin-top:40px}
.dots{position:absolute;left:568px;top:500px;display:flex;gap:10px}
.dots i{width:12px;height:12px;border-radius:50%;background:rgba(255,255,255,.5)}
.dots i:first-child{background:var(--white)}

/* welcome */
.welcome{top:730px;left:0;width:1200px;height:320px}
.welcome .brand{position:absolute;left:80px;top:120px;font-size:30px;color:var(--yellow)}
.welcome .brand .mark{width:24px;height:24px}
.welcome-body{position:absolute;left:520px;top:58px;width:600px}
.welcome-body p{color:var(--grey);margin:14px 0 26px;font-size:13px}

/* what we do */
.services{top:1010px;left:0;width:1200px;height:590px;background:linear-gradient(180deg,rgba(20,20,20,.93),rgba(20,20,20,.93)),linear-gradient(90deg,#555,#333);clip-path:polygon(0 60px,100% 0,100% 100%,0 calc(100% - 70px));color:var(--white);text-align:center}
.services .section-title{margin-top:150px}
.services .intro{width:840px;margin:14px auto 0;font-size:13px;color:#d0d0d0}
.service-row{display:flex;justify-content:center;gap:110px;margin-top:40px}
.service{width:260px}
.service h3{color:var(--yellow);font-size:15px;font-weight:900;margin:14px 0 6px;text-transform:uppercase}
.service p{font-size:12px;color:#d0d0d0}

/* products */
.products{top:1600px;left:0;width:1200px;height:550px}
.products-body{position:absolute;left:80px;top:110px;width:480px}
.products-body h3{font-size:15px;font-weight:900;margin-top:14px;text-transform:uppercase}
.products-body .tag{color:#c8b800;font-size:11px;font-weight:700;margin:4px 0 10px;text-transform:uppercase}
.products-body p{font-size:13px;color:var(--grey);margin-bottom:24px}
.products-art{position:absolute;left:640px;top:60px;width:480px;height:380px;background:radial-gradient(ellipse at 50% 55%,#cfe2f3 0%,#e8eff6 55%,#ffffff 80%)}

/* testimonials */
.testimonials{top:2150px;left:0;width:1200px;height:420px;background:var(--white)}
.testimonials svg{position:absolute;left:0;top:0}
.testimonials .section-title{position:absolute;left:80px;top:80px;font-size:32px}
.quotes{position:absolute;left:80px;top:180px;display:flex;gap:70px}
.quote{width:300px}
.quote p{font-size:13px;color:var(--grey)}
.person{display:flex;align-items:center;gap:14px;margin-top:20px}
.avatar{width:60px;height:60px;border-radius:50%;background:linear-gradient(135deg,#6d7a89,#c9cdd2)}
.person strong{display:block;font-size:15px;font-weight:900}
.person span{font-size:13px;color:var(--grey)}

/* press */
.press{top:2570px;left:0;width:1200px;height:310px;text-align:center}
.press h2{font-size:22px;font-weight:900;margin-top:30px}
.press-grid{display:grid;grid-template-columns:repeat(3,320px);justify-content:center;row-gap:44px;column-gap:30px;margin-top:40px}
.press-grid span{font-size:28px;font-weight:900;color:var(--ink);white-space:nowrap}

/* news */
.news{top:2880px;left:0;width:1200px;height:500px;background:var(--light)}
.news .section-title{text-align:center;margin-top:34px;font-size:32px}
.news-row{position:absolute;left:80px;top:110px;display:flex;gap:40px}
.card{width:320px;background:var(--white)}
.card .photo{height:190px;background:linear-gradient(135deg,#7d8ca0,#d5d9de)}
.card:nth-child(2) .photo{background:linear-gradient(135deg,#b8c2cc,#eef1f4)}
.card:nth-child(3) .photo{background:linear-gradient(135deg,#5f6f82,#b09a7a)}
.card-body{padding:16px 20px 24px;text-align:center}
.card-body h4{font-size:15px;font-weight:900;text-transform:uppercase}
.card-body .date{color:#c8b800;font-size:11px;font-weight:700;margin:4px 0 8px}
.card-body p{font-size:12px;color:var(--grey)}
.arrow{position:absolute;top:260px}

/* footer */
.footer{top:3380px;left:0;width:1200px;height:352px;background:var(--dark);color:var(--white)}
.newsletter{position:absolute;left:320px;top:-30px;width:880px;height:64px;background:var(--yellow);clip-path:polygon(30px 0,100% 0,100% 100%,0 100%);display:flex;align-items:center;gap:30px;padding-left:120px}
.newsletter h3{font-size:18px;font-weight:900;color:var(--ink)}
.newsletter .field{width:270px;height:36px;background:var(--white);font-size:12px;color:#888;padding:11px 12px}
.newsletter .submit{height:36px;background:var(--black);color:var(--white);font-size:12px;font-weight:700;padding:11px 16px;margin-left:-30px}
.footer .brand{position:absolute;left:70px;top:110px;color:var(--yellow);font-size:20px}
.copy{position:absolute;left:70px;top:150px;font-size:12px;color:#aaa;line-height:1.6}
.cols{position:absolute;left:350px;top:80px;display:flex;gap:60px}
.col h5{color:var(--yellow);font-size:14px;font-weight:900;margin-bottom:10px;text-transform:uppercase}
.col li{list-style:none;font-size:12px;color:#cfcfcf;line-height:1.9}
.footer svg.corner{position:absolute;left:0;bottom:0}
</style>
</head>
<body>

<div class="abs topbar">
  <span><svg width="12" height="12" viewBox="0 0 24 24"><path fill="#5c5c5c" d="M6.6 10.8a15 15 0 0 0 6.6 6.6l2.2-2.2c.3-.3.7-.4 1-.2 1.1.4 2.3.6 3.6.6.6 0 1 .4 1 1V20c0 .6-.4 1-1 1A17 17 0 0 1 3 4c0-.6.4-1 1-1h3.5c.6 0 1 .4 1 1 0 1.3.2 2.5.6 3.6.1.3 0 .7-.2 1z"/></svg>1 (800) 555-0142</span>
  <span><svg width="13" height="10" viewBox="0 0 26 20"><rect x="1" y="1" width="24" height="18" fill="none" stroke="#5c5c5c" stroke-width="2"/><path d="M1 1l12 10L25 1" fill="none" stroke="#5c5c5c" stroke-width="2"/></svg>info@memorialledger.example</span>
</div>

<header class="abs header">
  <div class="brand"><span class="mark"></span>Memorial Ledger Suite</div>
  <nav class="nav">
    <a class="active">Home</a><a>About Us</a><a>Products</a><a>Features</a><a>News</a><a>Contact Us</a><a class="login">Log In</a>
  </nav>
</header>

<section class="abs hero" role="img" aria-label="Photo of business professionals in a tense office meeting">
  <div class="hero-caption">
    <h1>MEMORIAL LEDGER SUITE</h1>
    <p>Maecenas consectetur felis pharetra libero interdum..</p>
    <span class="btn btn-yellow">Read More</span>
  </div>
  <div class="dots"><i></i><i></i><i></i></div>
</section>

<section class="abs welcome">
  <div class="brand"><span class="mark"></span>Memorial Ledger Suite</div>
  <div class="welcome-body">
    <h2 class="section-title">Welcome to our website</h2>
    <p>Proin tincidunt erat nec sapien commodo tristique. Sed nec tellus blandit, dapibus nisl sit amet, ultricies mauris. Cras mattis pulvinar luctus quisque vulputate mi ligula, id faucibus eros volutpat vitae. Proin accumsan eleifend leo, at sagittis turpis scelerisque. Vivamus suscipit velit eget turpis molestie, a lobortis enim ultricies.</p>
    <span class="btn btn-outline">Read More</span>
  </div>
</section>

<section class="abs services">
  <h2 class="section-title">What we do</h2>
  <p class="intro">Proin tincidunt erat nec sapien commodo tristique. Sed nec tellus blandit, dapibus nisl sit amet, ultricies mauris. Cras mattis pulvinar luctus quisque vulputate mi ligula, id faucibus eros volutpat.</p>
  <div class="service-row">
    <div class="service">
      <svg width="56" height="44" viewBox="0 0 56 44"><path fill="#fbee3d" d="M14 40a12 12 0 0 1-1-24 16 16 0 0 1 30 4 10 10 0 0 1-1 20z"/></svg>
      <h3>Malesuada Nulla</h3>
      <p>Sed tincidunt felis at nulla consequat, et posuere tortor vehicula rhoncus est vel euismod vestibulum.</p>
    </div>
    <div class="service">
      <svg width="56" height="44" viewBox="0 0 56 44"><rect x="4" y="2" width="48" height="30" rx="2" fill="#fbee3d"/><rect x="9" y="7" width="38" height="20" fill="#1c1c1c"/><rect x="22" y="34" width="12" height="4" fill="#fbee3d"/><rect x="14" y="38" width="28" height="4" fill="#fbee3d"/></svg>
      <h3>Malesuada Nulla</h3>
      <p>Sed tincidunt felis at nulla consequat, et posuere tortor vehicula rhoncus est vel euismod vestibulum.</p>
    </div>
    <div class="service">
      <svg width="56" height="44" viewBox="0 0 56 44"><circle cx="22" cy="24" r="12" fill="none" stroke="#fbee3d" stroke-width="7" stroke-dasharray="5 4"/><circle cx="22" cy="24" r="5" fill="#fbee3d"/><circle cx="42" cy="12" r="7" fill="none" stroke="#fbee3d" stroke-width="5" stroke-dasharray="3 3"/></svg>
      <h3>Malesuada Nulla</h3>
      <p>Sed tincidunt felis at nulla consequat, et posuere tortor vehicula rhoncus est vel euismod vestibulum.</p>
    </div>
  </div>
</section>

<section class="abs products">
  <div class="products-body">
    <h2 class="section-title">Products</h2>
    <h3>Vivamus suscipit velit eget turpis...</h3>
    <div class="tag">Sed nec tellus blandit, dapibus nisl sit amet ultricies</div>
    <p>Proin tincidunt erat nec sapien commodo tristique. Sed nec tellus blandit, dapibus nisl sit amet, ultricies mauris. Cras mattis pulvinar luctus quisque vulputate mi ligula, id faucibus eros volutpat vitae. Proin accumsan eleifend leo, at sagittis turpis scelerisque. Cras placerat lorem nec ligula fermentum interdum. Etiam sodales viverra eros eget lobortis.</p>
    <span class="btn btn-outline">More Info</span>
  </div>
  <div class="products-art" role="img" aria-label="Illustration of laptop, tablet and phone showing cloud software dashboards"></div>
</section>

<section class="abs testimonials">
  <svg width="1200" height="420" viewBox="0 0 1200 420"><polygon points="0,0 1200,0 1200,40 0,160" fill="#fbee3d"/><polygon points="1200,330 1200,420 960,420" fill="#fbee3d"/></svg>
  <h2 class="section-title">What our clients says..</h2>
  <div class="quotes">
    <div class="quote"><p>" Proin tincidunt erat nec sapien commodo tristique. Sed nec tellus blandit, dapibus nisl sit amet, ultricies mauris. Cras mattis pulvinar luctus quisque vulputate mi ligula."</p><div class="person"><div class="avatar" role="img" aria-label="Client portrait"></div><div><strong>NAME HEADING</strong><span>Company Name</span></div></div></div>
    <div class="quote"><p>" Proin tincidunt erat nec sapien commodo tristique. Sed nec tellus blandit, dapibus nisl sit amet, ultricies mauris. Cras mattis pulvinar luctus quisque vulputate mi ligula."</p><div class="person"><div class="avatar" role="img" aria-label="Client portrait"></div><div><strong>NAME HEADING</strong><span>Company Name</span></div></div></div>
    <div class="quote"><p>" Proin tincidunt erat nec sapien commodo tristique. Sed nec tellus blandit, dapibus nisl sit amet, ultricies mauris. Cras mattis pulvinar luctus quisque vulputate mi ligula."</p><div class="person"><div class="avatar" role="img" aria-label="Client portrait"></div><div><strong>NAME HEADING</strong><span>Company Name</span></div></div></div>
  </div>
</section>

<section class="abs press">
  <h2>AS SEEN ON</h2>
  <div class="press-grid">
    <span>Northgate Bulletin</span><span>Circuit Weekly</span><span>Tallyworth</span>
    <span>Harborfield Books</span><span>The Capital Courier</span><span>Brightpace Journal</span>
  </div>
</section>

<section class="abs news">
  <h2 class="section-title">News</h2>
  <svg class="arrow" style="left:30px" width="20" height="30" viewBox="0 0 20 30"><path d="M16 3L4 15l12 12" fill="none" stroke="#222" stroke-width="4"/></svg>
  <svg class="arrow" style="left:1150px" width="20" height="30" viewBox="0 0 20 30"><path d="M4 3l12 12L4 27" fill="none" stroke="#222" stroke-width="4"/></svg>
  <div class="news-row">
    <article class="card"><div class="photo" role="img" aria-label="Photo of a team gathered around a laptop"></div><div class="card-body"><h4>Vivamus suscipit velit</h4><div class="date">APR 18, 2019</div><p>Sed nec tellus blandit, dapibus nisl sit amet, ultricies mauris lorem ipsum.</p></div></article>
    <article class="card"><div class="photo" role="img" aria-label="Photo of a hand pointing at a laptop screen"></div><div class="card-body"><h4>Vivamus suscipit velit</h4><div class="date">APR 18, 2019</div><p>Sed nec tellus blandit, dapibus nisl sit amet, ultricies mauris lorem ipsum.</p></div></article>
    <article class="card"><div class="photo" role="img" aria-label="Photo of colleagues working at a desk"></div><div class="card-body"><h4>Vivamus suscipit velit</h4><div class="date">APR 18, 2019</div><p>Sed nec tellus blandit, dapibus nisl sit amet, ultricies mauris lorem ipsum.</p></div></article>
  </div>
</section>

<footer class="abs footer">
  <div class="newsletter"><h3>NEWSLETTER SIGN UP</h3><div class="field">Enter Email Address</div><div class="submit">SIGN UP</div></div>
  <div class="brand"><span class="mark"></span>Memorial Ledger Suite</div>
  <div class="copy">Copyright © 2019 Company Name<br>All Rights reserved</div>
  <div class="cols">
    <div class="col"><h5>Navigation</h5><ul><li>Home</li><li>About Us</li><li>Products</li><li>Features</li><li>News</li><li>Contact Us</li></ul></div>
    <div class="col"><h5>Features</h5><ul><li>Vivamus et nisi</li><li>Gravida ultrices</li><li>Ante volutpat sed</li><li>Vivamus nisl</li><li>Lorem erat</li></ul></div>
    <div class="col"><h5>Resources</h5><ul><li>Vivamus et nisi</li><li>Gravida ultrices</li><li>Ante volutpat sed</li><li>Vivamus nisl</li><li>Lorem erat</li></ul></div>
    <div class="col"><h5>Contact Info</h5><ul><li>48 Harbor Lane, Suite 5,</li><li>Springfield, USA</li><li>1 (800) 555-0142</li><li>info@memorialledger.example</li><li>Map Location</li></ul></div>
  </div>
  <svg class="corner" width="260" height="110" viewBox="0 0 260 110"><polygon points="0,20 260,110 0,110" fill="#fbee3d"/></svg>
</footer>

</body>
</html>
```